Business card required for IT Consultancy Business - Tealbrook Consulting.
Company provides the whole nine yards of services across IT Architecture, design and execution.
Basically we provide consulting services to help businesses make sure their technology is enabling their business strategy.
Design for front and back required.
We would like the front of the card to inlcude:
Name
Title
Mobile number
email address
www.tbkc.com.au
Company logos attached.
Thank you
Industry/Entity Type
Business
Contact Information for Business Card
Name
Title
Mobile number
email address
www.tbkc.com.au
Look and feel
Each slider illustrates characteristics of the customer's brand and the style your logo design should communicate.

```html
<!DOCTYPE html>
<html lang="en">
<head>
<meta charset="utf-8">
<title>Tealbrook Consulting – Business Card</title>
<link rel="stylesheet" href="https://fonts.googleapis.com/css2?family=Montserrat:wght@400;500;700&family=Oswald:wght@500&display=swap">
<style>
  :root {
    --backdrop: #3b3b3d;
    --card-white: #ffffff;
    --card-black: #0a0b0d;
    --brand-blue: #1a7bc4;
    --brand-orange: #f05a22;
    --text-grey: #6b6b6b;
    --text-light: #f2f2f2;
    --rule: #bfbfbf;
  }
  * { box-sizing: border-box; margin: 0; padding: 0; }
  html, body {
    width: 1200px; height: 864px; overflow: hidden;
    background: var(--backdrop);
  }
  .canvas {
    width: 1200px; height: 864px;
    display: flex; flex-direction: column;
    align-items: center; justify-content: center; gap: 40px;
  }
  .card {
    width: 560px; height: 320px;
    border-radius: 22px;
    position: relative;
    box-shadow: 0 14px 30px rgba(0,0,0,.45);
  }
  /* Front: company name */
  .card--front {
    background: var(--card-white);
    display: flex; flex-direction: column; align-items: center; justify-content: center;
  }
  .wordmark {
    display: flex; align-items: center; gap: 14px;
    font-family: "Montserrat", sans-serif; font-weight: 700;
    font-size: 34px; letter-spacing: .5px;
    color: var(--brand-blue);
    margin-top: 10px;
  }
  .wordmark__dot {
    width: 26px; height: 26px; border-radius: 50%;
    background: var(--brand-orange);
  }
  .website-front {
    position: absolute; bottom: 52px; left: 0; right: 0; text-align: center;
    font-family: "Montserrat", sans-serif; font-size: 14px; font-weight: 500;
    color: var(--text-grey); letter-spacing: .5px;
  }
  /* Back: contact */
  .card--back {
    background: var(--card-black);
    display: flex; align-items: center; justify-content: center; gap: 18px;
  }
  .identity { text-align: right; }
  .identity__name {
    font-family: "Oswald", sans-serif; font-weight: 500;
    font-size: 34px; line-height: 1; color: var(--brand-blue); letter-spacing: .3px;
  }
  .identity__title {
    font-family: "Montserrat", sans-serif; font-size: 14px; font-weight: 500;
    color: var(--text-light); margin-top: 4px; letter-spacing: .5px;
  }
  .divider { width: 1px; height: 64px; background: var(--rule); }
  .contact { list-style: none; display: flex; flex-direction: column; gap: 5px; }
  .contact__item {
    display: flex; align-items: center; gap: 8px;
    font-family: "Montserrat", sans-serif; font-size: 14px; color: var(--text-light);
  }
  .contact__icon { width: 13px; height: 13px; flex: none; }
</style>
</head>
<body>
<main class="canvas">
  <section class="card card--front" aria-label="Card front">
    <div class="wordmark"><span class="wordmark__dot"></span>Tealbrook Consulting</div>
    <p class="website-front">www.tbkc.com.au</p>
  </section>

  <section class="card card--back" aria-label="Card back">
    <div class="identity">
      <h1 class="identity__name">DANIEL MARLOWE</h1>
      <p class="identity__title">President</p>
    </div>
    <div class="divider"></div>
    <ul class="contact">
      <li class="contact__item">
        <svg class="contact__icon" viewBox="0 0 14 14"><rect x="3.5" y="1" width="7" height="12" rx="1.2" fill="none" stroke="var(--brand-orange)" stroke-width="1.4"/><circle cx="7" cy="11" r=".8" fill="var(--brand-orange)"/></svg>
        013-482-5710
      </li>
      <li class="contact__item">
        <svg class="contact__icon" viewBox="0 0 14 14"><rect x="1" y="3" width="12" height="8.5" fill="var(--brand-orange)"/><path d="M1 3 L7 8 L13 3" fill="none" stroke="var(--card-black)" stroke-width="1.1"/></svg>
        info@tbkc.com.au
      </li>
      <li class="contact__item">
        <svg class="contact__icon" viewBox="0 0 14 14" fill="none" stroke="var(--brand-orange)" stroke-width="1.2"><circle cx="7" cy="7" r="5.8"/><ellipse cx="7" cy="7" rx="2.6" ry="5.8"/><path d="M1.2 7 H12.8"/></svg>
        www.tbkc.com.au
      </li>
    </ul>
  </section>
</main>
</body>
</html>
```